Looking for a high-end business card design for a construction company

We are looking to update our business card design. We are a post-frame construction company that builds custom buildings, commercial spaces, homes, and anything else. We have multiple people working here so we would need something we can easily customize the information for the specific person. We need a name, website, cell phone, office phone as well as social icons. Our colors are black, white, and grey/silver so I would love a black background or something that is more striking than just a traditional white business card. Looking for something that is very professional with a high-end look/feel. I have attached our logos, they can be silver, white, grey, or black.
Industry/Entity Type
Construction
Contact Information for Business Card
Business logo, Name, Cell phone, Office phone, website, social Icons
Colors
Designer to choose only greyscale colors for use in the design.
Look and feel

```html
<!DOCTYPE html>
<html lang="en">
<head>
<meta charset="UTF-8">
<title>Halvorsen Builders, Inc. — Business Card</title>
<link rel="stylesheet" href="https://fonts.googleapis.com/css2?family=Montserrat:wght@400;600&display=swap">
<style>
  :root {
    --stage: #3a3330;
    --card: #1b1c1e;
    --ink: #f2f2f2;
    --ink-soft: #d6d6d6;
    --silver: #b9bcc0;
    --rule: #8a8c8f;
  }
  * { margin: 0; padding: 0; box-sizing: border-box; }
  html, body {
    width: 1200px; height: 769px; overflow: hidden;
    background: var(--stage);
    font-family: "Montserrat", sans-serif;
  }
  .stage {
    position: relative; width: 1200px; height: 769px;
    display: flex; align-items: center; justify-content: center; gap: 60px;
  }
  .card {
    position: relative;
    width: 520px; height: 297px;
    background: var(--card);
    border-radius: 3px;
    box-shadow: 0 14px 30px rgba(0,0,0,.45);
  }
  /* Front: contact side */
  .card-front { display: flex; align-items: center; }
  .brand {
    width: 250px; padding-left: 40px;
    display: flex; align-items: center; gap: 12px;
  }
  .brand-dot {
    flex: none; width: 18px; height: 18px; border-radius: 50%;
    background: var(--ink);
  }
  .brand-name {
    color: var(--ink); font-weight: 600;
    font-size: 20px; line-height: 1.15; letter-spacing: .06em;
    text-transform: uppercase;
  }
  .divider {
    width: 1px; height: 170px; background: var(--rule);
  }
  .contact { padding-left: 26px; }
  .person {
    color: var(--ink); font-weight: 600; font-size: 15px;
    letter-spacing: .03em; text-transform: uppercase;
    margin-bottom: 16px;
  }
  .contact-list { list-style: none; }
  .contact-item {
    display: flex; align-items: center; gap: 10px;
    color: var(--ink-soft); font-size: 12.5px; font-weight: 400;
    line-height: 1; margin-bottom: 8px;
  }
  .contact-item svg { width: 12px; height: 12px; flex: none; fill: var(--ink-soft); }
  /* Back: brand side */
  .card-back {
    display: flex; align-items: center; justify-content: center; gap: 16px;
  }
  .card-back .brand-dot { width: 34px; height: 34px; background: var(--silver); }
  .card-back .brand-name { color: var(--silver); font-size: 28px; }
</style>
</head>
<body>
<main class="stage">
  <section class="card card-front" aria-label="Business card, contact side">
    <div class="brand">
      <span class="brand-dot"></span>
      <span class="brand-name">Halvorsen<br>Builders, Inc.</span>
    </div>
    <div class="divider"></div>
    <div class="contact">
      <h1 class="person">Daniel Reyes</h1>
      <ul class="contact-list">
        <li class="contact-item">
          <svg viewBox="0 0 24 24" aria-hidden="true"><path d="M6.6 10.8a15.1 15.1 0 0 0 6.6 6.6l2.2-2.2a1 1 0 0 1 1-.25 11.4 11.4 0 0 0 3.6.57 1 1 0 0 1 1 1V20a1 1 0 0 1-1 1A17 17 0 0 1 3 4a1 1 0 0 1 1-1h3.5a1 1 0 0 1 1 1c0 1.25.2 2.45.57 3.57a1 1 0 0 1-.25 1z"/></svg>
          555-214-7730
        </li>
        <li class="contact-item">
          <svg viewBox="0 0 24 24" aria-hidden="true"><path d="M7 1h10a2 2 0 0 1 2 2v18a2 2 0 0 1-2 2H7a2 2 0 0 1-2-2V3a2 2 0 0 1 2-2zm0 3v14h10V4zm5 15.5a1 1 0 1 0 0 2 1 1 0 0 0 0-2z"/></svg>
          555-318-4096
        </li>
        <li class="contact-item">
          <svg viewBox="0 0 24 24" aria-hidden="true"><path d="M2 5h20v14H2zm2 2v.5l8 5 8-5V7zm0 3v7h16v-7l-8 5z"/></svg>
          info@halvorsenbuilders.com
        </li>
        <li class="contact-item">
          <svg viewBox="0 0 24 24" aria-hidden="true"><path d="M12 2a10 10 0 1 0 0 20 10 10 0 0 0 0-20zm6.9 9h-3a15 15 0 0 0-1.3-5.6A8 8 0 0 1 18.9 11zM12 4.1A13 13 0 0 1 13.9 11h-3.8A13 13 0 0 1 12 4.1zM9.4 5.4A15 15 0 0 0 8.1 11h-3a8 8 0 0 1 4.3-5.6zM5.1 13h3a15 15 0 0 0 1.3 5.6A8 8 0 0 1 5.1 13zm6.9 6.9a13 13 0 0 1-1.9-6.9h3.8a13 13 0 0 1-1.9 6.9zm2.6-1.3a15 15 0 0 0 1.3-5.6h3a8 8 0 0 1-4.3 5.6z"/></svg>
          www.halvorsenbuilders.com
        </li>
      </ul>
    </div>
  </section>

  <section class="card card-back" aria-label="Business card, brand side">
    <span class="brand-dot"></span>
    <span class="brand-name">Halvorsen<br>Builders, Inc.</span>
  </section>
</main>
</body>
</html>
```